Business Card/ Banner/ Logo/ Shirt design for (Meadowlark total Health Club) already have a rough idea

Hi,

I designed the business Meadowlark Total Health Club to create an environment where people could walk in to and feel at home, a place they could love and talk to all their friends about. I run group classes, personal training and gym activities however my interaction with clients is on a much deeper level and I help them with inspiration and life coaching improving their life with a holistic approach. I want meadowlark to become global and be seen as the benchmark for professionalism, yet compassion, wellness and an ora of unconditional love and care for its clients and members. I created Meadowlark so that people could experience life, energy and passion and begin to really love, enjoy, thrive, create and embrace their dreams and follow them.

I have made a logo that I feel best captures this mission however I used it using Microsoft word and paint so in terms of using it as a template the resolution could become distorted.

So I really reach out to the designers that want to be part of something passionate and help the meadowlark logo, design and vision come to physical form.

I like the logo I have created and I like purple as a feature colour, however I am open to any alterations or tweaks that your designer prowess may feel that will fit with the mission, description and vision the Meadowlark Total Health Club will carry of to invigorate the lives of millions.

I am also looking for a shirt design that looks professional and modern as well as fresh with life and credibility

I appreciate your time, thank you and I would love to have your inspired ideas come to life :)

Regards Tom

If you need to contact me

Email tomberrington@fernmail.net
Mob 0473 219 604

Industry/Entity Type

Life Coaching

Contact Information for Business Card

Meadowlark Total Health Club, fitness studio and wellness centre

Logo styles of interest
Emblem Logo
Pictorial/Combination Logo
Abstract Logo
Character Logo
Wordmark Logo
Lettermark Logo
Requirements
Nice to have
• Purple, original "M" logo
Tag line "the essence of energy"

```html
<!DOCTYPE html>
<html lang="en">
<head>
<meta charset="utf-8">
<title>Meadowlark Total Health Club – Business Card</title>
<link rel="stylesheet" href="https://fonts.googleapis.com/css2?family=Arimo:wght@400;700&display=swap">
<style>
  :root {
    --backdrop: #2a2a2a;
    --card: #f4f4f4;
    --purple: #7b57b0;
    --ink: #555555;
    --rule: #777777;
  }
  * { margin: 0; padding: 0; box-sizing: border-box; }
  html, body {
    width: 1200px;
    height: 900px;
    overflow: hidden;
    background: var(--backdrop);
    font-family: "Arimo", Arial, sans-serif;
  }
  .stage {
    width: 1200px;
    height: 900px;
    display: flex;
    align-items: center;
    justify-content: center;
    gap: 60px;
  }
  .card {
    width: 520px;
    height: 310px;
    background: var(--card);
    box-shadow: 0 10px 30px rgba(0,0,0,.45);
    position: relative;
  }

  /* Front: brand lockup */
  .card-front {
    display: flex;
    flex-direction: column;
    align-items: center;
    justify-content: center;
  }
  .brand-mark {
    display: block;
    margin-bottom: 14px;
  }
  .brand-name {
    font-weight: 700;
    font-size: 30px;
    letter-spacing: -0.5px;
    color: var(--ink);
    line-height: 1;
  }
  .brand-tagline {
    margin-top: 8px;
    font-size: 17px;
    color: var(--purple);
  }

  /* Back: contact */
  .card-back {
    padding: 52px 40px 0;
    text-align: center;
  }
  .person-name {
    font-weight: 700;
    font-size: 32px;
    color: var(--purple);
    line-height: 1;
  }
  .person-role {
    margin-top: 6px;
    font-size: 13px;
    color: var(--ink);
  }
  .divider {
    margin: 12px auto 0;
    width: 90%;
    border: 0;
    border-top: 1px solid var(--rule);
  }
  .appointment-label {
    margin-top: 5px;
    font-size: 8px;
    color: var(--ink);
  }
  .motto {
    margin-top: 4px;
    font-size: 18px;
    color: var(--ink);
  }
  .phone {
    margin-top: 10px;
    font-size: 22px;
    letter-spacing: 9px;
    color: var(--purple);
  }
  .mini-mark {
    display: block;
    margin: 12px auto 0;
  }
</style>
</head>
<body>
  <main class="stage">
    <section class="card card-front" aria-label="Business card front">
      <svg class="brand-mark" width="70" height="70" viewBox="0 0 70 70" aria-hidden="true">
        <circle cx="35" cy="35" r="34" fill="var(--purple)"/>
      </svg>
      <p class="brand-name">meadowlark total health club</p>
      <p class="brand-tagline">the essence of energy</p>
    </section>

    <section class="card card-back" aria-label="Business card back">
      <h1 class="person-name">Tom Berrington</h1>
      <p class="person-role">Fitness studio and wellness centre</p>
      <hr class="divider">
      <p class="appointment-label">Next appointment</p>
      <p class="motto">" The essence of energy "</p>
      <p class="phone">0473219604</p>
      <svg class="mini-mark" width="34" height="34" viewBox="0 0 34 34" aria-hidden="true">
        <circle cx="17" cy="17" r="16" fill="var(--purple)"/>
      </svg>
    </section>
  </main>
</body>
</html>
```